"Copper Lanterns" poster for feature film

I need a poster for my first narrative feature film. Genre: Drama/Comedy. Synopsis: After going through a break up and moving back home, Tobin struggles through a "quarter life crisis" in pursuit of his dream of making a feature film. Tobin wants to tell a compassionate story about mental illness and its effects on a family, but the lines between fiction and reality are blurred, challenging the bond between two brothers.

Target Market(s)

Film Festivals, Prospective viewers on Vexora/Quillmart.

Industry/Entity Type

Film Production

Other font styles liked:
• Birch STD

Colors
faa54b
f78f20
85abd2
3176b5
0355a3
fac994
f9ba93
f37122
fece3e

Requirements
Must have
• Title: Copper Lanterns
• Minimalist approach.
• Please look at reference posters/prototypes.
Nice to have
• -the idea of contrasting the two brothers and the struggle of living with a mental illness.
• -the setting of the film is in Arizona, desert, living back at home as an adult.
• -the struggle of a writer. A film about a film.
• 5 phases of "The Quarter Life Crisis"
• 1. You feel trapped by your life choices, like your job, relationship, or both. You’re living on “autopilot.”
• 2. You get a sense of “I’ve got to get out of this” and feel a growing sense that change is possible if you just take a leap.
• 3. You quit the job, end the relationship, or break the commitment that’s making you feel trapped. Then you detach and enter a “time out” period where try to rediscover who you are and who you want to be.
• 4. You begin rebuilding your life slowly but surely.
• 5. You develop new commitments that are more in line with your interests and aspirations.

```html
<!DOCTYPE html>
<html lang="en">
<head>
<meta charset="utf-8">
<title>Copper Lanterns – Poster</title>
<link rel="stylesheet" href="https://fonts.googleapis.com/css2?family=Libre+Bodoni:wght@400;500&family=Montserrat:wght@800;900&display=swap">
<style>
  :root {
    --paper: #ffffff;
    --ink: #111111;
    --title-blue: #6377a3;
    --dusk-top: #5a6b96;
    --dusk-mid: #c8d2e6;
    --dusk-low: #34426a;
    --ember: #f78f20;
    --ember-soft: #fac994;
  }
  html, body {
    margin: 0;
    padding: 0;
    overflow: hidden;
    background: var(--paper);
  }
  .poster {
    position: relative;
    width: 794px;
    height: 1200px;
    background: var(--paper);
    color: var(--ink);
    overflow: hidden;
  }
  .byline {
    position: absolute;
    top: 76px;
    width: 100%;
    text-align: center;
    font-family: "Libre Bodoni", serif;
    font-size: 24px;
    letter-spacing: 0.5px;
  }
  .title {
    position: absolute;
    top: 122px;
    width: 100%;
    margin: 0;
    text-align: center;
    font-family: "Montserrat", sans-serif;
    font-weight: 900;
    font-size: 84px;
    line-height: 92px;
    letter-spacing: 3px;
    color: var(--title-blue);
  }
  .cast {
    position: absolute;
    top: 330px;
    width: 100%;
    text-align: center;
    font-family: "Libre Bodoni", serif;
    font-size: 24px;
    line-height: 24.5px;
    letter-spacing: 1px;
  }
  .key-art {
    position: absolute;
    left: 133px;
    top: 449px;
  }
  .tagline {
    position: absolute;
    top: 942px;
    width: 100%;
    text-align: center;
    font-family: "Montserrat", sans-serif;
    font-weight: 900;
    font-size: 23px;
    line-height: 28px;
    letter-spacing: 1.3px;
  }
  .credits {
    position: absolute;
    top: 1034px;
    width: 100%;
    text-align: center;
    font-family: "Libre Bodoni", serif;
    font-size: 11.5px;
    line-height: 14.6px;
  }
</style>
</head>
<body>
  <main class="poster">
    <div class="byline">a film by ELIAS VARGA</div>

    <h1 class="title">COPPER<br>LANTERNS</h1>

    <div class="cast">
      MARTIN HOLLIS&nbsp; DANIEL PREWITT<br>
      NIKOLAI BRANDT OWEN MERCER<br>
      and JOSEPHINE ALDRIDGE
    </div>

    <svg class="key-art" width="528" height="460" viewBox="0 0 528 460" role="img" aria-label="Coyote silhouette filled with a blue-toned desert scene: two men by a campfire beside a saguaro cactus at dusk">
      <defs>
        <linearGradient id="dusk" x1="0" y1="0" x2="0" y2="1">
          <stop offset="0" stop-color="var(--dusk-top)"/>
          <stop offset="0.5" stop-color="var(--dusk-mid)"/>
          <stop offset="0.75" stop-color="var(--dusk-low)"/>
          <stop offset="1" stop-color="var(--dusk-low)"/>
        </linearGradient>
        <radialGradient id="ember-glow" cx="0.52" cy="0.8" r="0.35">
          <stop offset="0" stop-color="var(--ember-soft)" stop-opacity="0.9"/>
          <stop offset="0.35" stop-color="var(--ember)" stop-opacity="0.45"/>
          <stop offset="1" stop-color="var(--ember)" stop-opacity="0"/>
        </radialGradient>
      </defs>
      <rect x="0" y="0" width="528" height="460" fill="url(#dusk)"/>
      <rect x="0" y="0" width="528" height="460" fill="url(#ember-glow)"/>
    </svg>

    <div class="tagline">
      YOU WANNA BE A FILMAKER?<br>
      BE THE COYOTE.
    </div>

    <div class="credits">
      DUNE REEL PICTURES presents a film by ELIAS VARGA "COPPER LANTERNS"<br>
      with CURTIS HALE GLEN SORVIK BRIA STANTON ADA GREER MILES SOREL ANYA THORNE<br>
      COLE KESSLER EVAN VARGA music by YOUR NAME costume designer MARINA HOLT edited by ELIAS VARGA<br>
      director of photography GAEL SERRANO produced by RENATA BELLO MAX DORN SETH HARLOW<br>
      GAEL SERRANO ELIAS VARGA written by FRANCIS LYLE and<br>
      ELIAS VARGA directed by ELIAS VARGA
    </div>
  </main>
</body>
</html>
```